U.S. Popcorn company needs business cards

We are a popcorn company that manufactures popcorn and sells it to grocery stores worldwide. Our theme is "Americana" and our logo is U.S. route 66 which is the most famous highway in the U.S.

We would like the design to be simple and to use both sides. On the back side we would like to see just the logo and website. The front would be normal details

Target Market(s)

Wholesalers, grocers and distributors

Industry/Entity Type

Manufacture

Contact Information for Business Card

Business name: Bluebell Ridge Popcorn
Phone: +1 555 014 2286
Email: Derek@bluebellridgepopcorn.com
website: www.bluebellridgepopcorn.com
Tag Line: "POPping since day one"
Name: Derek Halvorsen
Title: Founder/President

Requirements
Must have
• Either this design should be fun or clean and simple. I will let you show me your thougths.
Nice to have
• Anything that ties in the real Hwy Route 66.
• Colors might need to be red, white and blue incorporated.
Should not have
• Not be too busy.

```html
<!DOCTYPE html>
<html lang="en">
<head>
<meta charset="utf-8">
<title>Bluebell Ridge Popcorn – Business Cards</title>
<link rel="stylesheet" href="https://fonts.googleapis.com/css2?family=Mulish:wght@400;600;800&display=swap">
<style>
  :root {
    --backdrop: #1e1e1e;
    --card-black: #141414;
    --navy: #17306b;
    --red: #d9211f;
    --white: #ffffff;
    --silver: #8a8a8a;
    --text-light: #e6e6e6;
  }
  * { margin: 0; padding: 0; box-sizing: border-box; }
  html, body {
    width: 1200px; height: 793px; overflow: hidden;
    background: var(--backdrop);
    font-family: "Mulish", sans-serif;
  }
  .canvas {
    position: relative; width: 1200px; height: 793px;
    display: flex; align-items: center; justify-content: center; gap: 50px;
  }
  .card {
    position: relative; width: 520px; height: 300px;
    border-radius: 12px; overflow: hidden;
    background: var(--card-black);
  }
  /* Back side */
  .card-back { display: flex; align-items: center; justify-content: center; }
  .brand-back {
    display: flex; align-items: center; gap: 10px;
    color: var(--silver); font-weight: 800; font-size: 22px; letter-spacing: 0.5px;
  }
  .brand-back .dot { width: 14px; height: 14px; border-radius: 50%; background: var(--silver); }
  /* Front side */
  .front-shape { position: absolute; inset: 0; }
  .brand-front {
    position: absolute; left: 26px; top: 0; width: 170px; height: 300px;
    display: flex; flex-direction: column; align-items: center; justify-content: center; gap: 10px;
    color: var(--white); font-weight: 800; font-size: 21px; line-height: 1.15; text-align: center;
  }
  .brand-front .dot { width: 16px; height: 16px; border-radius: 50%; background: var(--white); }
  .holder {
    position: absolute; right: 28px; top: 34px; text-align: right;
  }
  .holder-name { color: var(--red); font-weight: 800; font-size: 18px; }
  .holder-title { color: var(--text-light); font-size: 12px; margin-top: 2px; }
  .contact {
    position: absolute; right: 28px; bottom: 50px; text-align: right;
    color: var(--text-light); font-size: 12px; line-height: 1.6;
  }
  .contact li { list-style: none; display: flex; justify-content: flex-end; align-items: center; gap: 6px; }
  .contact svg { width: 11px; height: 11px; fill: var(--red); flex: none; }
  .contact .accent { color: var(--red); }
  .tagline {
    position: absolute; right: 28px; bottom: 22px;
    color: var(--text-light); font-size: 14px;
  }
  .tagline .accent { color: var(--red); font-weight: 800; }
</style>
</head>
<body>
<main class="canvas">
  <section class="card card-back" aria-label="Card back">
    <div class="brand-back"><span class="dot"></span>Bluebell Ridge Popcorn</div>
  </section>

  <section class="card card-front" aria-label="Card front">
    <svg class="front-shape" viewBox="0 0 520 300" aria-hidden="true">
      <path d="M0 0 H198 C250 60 268 180 272 300 H0 Z" fill="#d9211f"/>
      <path d="M0 0 H184 C236 60 256 180 262 300 H0 Z" fill="#17306b"/>
    </svg>
    <div class="brand-front"><span class="dot"></span>Bluebell Ridge<br>Popcorn</div>

    <div class="holder">
      <p class="holder-name">Derek Halvorsen</p>
      <p class="holder-title">Founder/President</p>
    </div>

    <ul class="contact">
      <li>+1 555 014 2286
        <svg viewBox="0 0 24 24"><path d="M6.6 10.8a15 15 0 0 0 6.6 6.6l2.2-2.2a1 1 0 0 1 1-.25 11.4 11.4 0 0 0 3.6.57 1 1 0 0 1 1 1V20a1 1 0 0 1-1 1A17 17 0 0 1 3 4a1 1 0 0 1 1-1h3.5a1 1 0 0 1 1 1c0 1.25.2 2.45.57 3.57a1 1 0 0 1-.25 1z"/></svg>
      </li>
      <li>Derek@bluebellridgepopcorn.com
        <svg viewBox="0 0 24 24"><path d="M2 5h20v14H2z M4 7v.5l8 5 8-5V7l-8 5z" fill-rule="evenodd"/></svg>
      </li>
      <li><span>www.<span class="accent">bluebellridgepopcorn</span>.com</span>
        <svg viewBox="0 0 24 24"><circle cx="12" cy="12" r="10"/><path d="M2 12h20M12 2c3 3 3 17 0 20M12 2c-3 3-3 17 0 20" stroke="#141414" stroke-width="1.5" fill="none"/></svg>
      </li>
    </ul>

    <p class="tagline">"<span class="accent">POP</span>ping since day one"</p>
  </section>
</main>
</body>
</html>
```